Figure for Manufacture of Wound Healing Gel

Who we are: We are a nationally funded bioengineering laboratory at Harwell Crest University conducting research on the tendon healing properties of a gel manufactured from real tendon.

What we need: We require a figure piece that will be included in an academic publication. With that in mind, the figure must be professional, clear, and concise. A reader would need to glance at the figure for only a moment to understand the process of how we manufacture and store tendon gel. Actual pictures of the in-between steps are included and will need to be cropped to improve the professional look of the design.

The Details: The figure should stepwise show the process of how we manufacture and store tendon gel. In brief, we harvest tendon from donor cadavers. Those tendons undergo decellularization, lyophilization (fancy word for freeze-drying), and are milled into a fine powder. The powder is set in acidified water and treated with digestive enzymes. After 24 hrs, the gel is brought to physiologic pH and salinity and placed in vials. The vials are frozen and again lyophilized (this is so they can be stored and transported easily). Finally the samples are reconstituted with DI water.

The Figure: Should be a linear process (horizontal). The following are the actual steps we wish to include (steps need not be numbered necessarily as long as they are in logical order...

1.) A picture of harvested tendon (Step 1.jpg)
2.) Written description: "Decellularization, lyophilization, and milling"
3.) A picture of milled tendon powder (Step 2.jpg)
4.) Written description: "Digestion with pepsin before establishing physiologic pH and salinity".
5.) A picture of gel (Step 3.jpg)
6.) Written description: "Lyophilization of aliquots"
7.) A picture of freeze-dried gel (Step 4.jpg)
8.) Written description: "Reconstitution with DI water"
9.) A picture of reconstituted gel (Step 5.jpg)

Feel free to message for any questions, comments, or clarifications.

```html
<!DOCTYPE html>
<html lang="en">
<head>
<meta charset="utf-8">
<title>Tendon Healing – Gel Manufacture</title>
<link href="https://fonts.googleapis.com/css2?family=Arimo:wght@400;700&display=swap" rel="stylesheet">
<style>
  :root{
    --brand:#e9461c;
    --caption:#f07c1e;
    --ink:#111111;
    --paper:#ffffff;
    --photo-light:#d9dde0;
    --photo-mid:#aeb4b9;
  }
  *{box-sizing:border-box;margin:0;padding:0}
  html,body{width:1200px;height:748px;overflow:hidden;background:var(--paper)}
  body{font-family:"Arimo",Arial,sans-serif;position:relative}
  .figure{position:absolute;left:38px;top:62px;width:1122px;height:619px;border:2px solid var(--brand)}
  .header{position:absolute;left:-2px;top:-2px;width:380px;height:50px;background:var(--brand);
    clip-path:polygon(0 0,100% 0,100% 100%,0 100%);color:var(--paper);padding:5px 10px}
  .header h1{font-size:20px;font-weight:700;line-height:22px}
  .header p{font-size:14px;line-height:17px}
  .footer{position:absolute;left:-2px;right:-2px;bottom:-2px;height:42px;background:var(--brand);
    color:var(--paper);font-size:10.2px;line-height:14px;padding:7px 12px;text-align:center}
  .step-photo{position:absolute;width:185px;height:185px;border:5px solid var(--brand);padding:6px;background:var(--paper)}
  .step-photo.top{border-radius:50% 50% 50% 0}
  .step-photo.bottom{border-radius:0 50% 50% 50%}
  .step-photo .photo{width:100%;height:100%;border-radius:50%;
    background:radial-gradient(circle at 50% 50%,var(--photo-light),var(--photo-mid))}
  .photo.tendon{background:radial-gradient(circle,#efe6c6 0,#c9c4b3 55%,#9ea3a6 100%)}
  .photo.powder{background:radial-gradient(circle,#f4ecc0 0,#cfccbd 50%,#9ea3a6 100%)}
  .photo.gel{background:radial-gradient(circle,#f3f1ea 0,#c8cccf 55%,#9ea3a6 100%)}
  .photo.vial{background:linear-gradient(180deg,#f4f4f4 0,#e6ddc0 60%,#f2f2f2 100%)}
  .rule{position:absolute;background:var(--brand)}
  .h{height:2px}.v{width:2px}
  .label{position:absolute;white-space:nowrap}
  .label .title{font-size:14px;color:var(--ink);line-height:16px}
  .label .desc{font-size:11.5px;color:var(--caption);line-height:13px;margin-top:6px}
</style>
</head>
<body>
<section class="figure">
  <header class="header">
    <h1>Tendon Healing</h1>
    <p>Gel Manufactured From Real Tendon.</p>
  </header>
  <footer class="footer">Those tendons undergo decellularization, lyophilization (fancy word for freeze-drying), and are milled into a fine powder. The powder is set in acidified water and treated with digestive enzymes. After 24 hrs, the gel is brought to physiologic pH and salinity and placed in vials. The vials are frozen and again lyophilized (this is so they can be stored and transported easily). Finally the samples are reconstituted with DI water.</footer>
</section>

<div class="step-photo top" style="left:84px;top:146px"><div class="photo tendon" role="img" aria-label="Harvested tendon strands in a glass dish"></div></div>
<div class="step-photo bottom" style="left:300px;top:412px"><div class="photo powder" role="img" aria-label="Milled tendon powder in a glass dish"></div></div>
<div class="step-photo top" style="left:540px;top:146px"><div class="photo gel" role="img" aria-label="Tendon gel in a glass dish"></div></div>
<div class="step-photo bottom" style="left:732px;top:412px"><div class="photo vial" role="img" aria-label="Vial of freeze-dried gel with red cap"></div></div>
<div class="step-photo top" style="left:925px;top:146px"><div class="photo vial" role="img" aria-label="Vial of reconstituted gel with red cap"></div></div>

<div class="rule h" style="left:88px;top:350px;width:209px"></div>
<div class="rule v" style="left:295px;top:350px;height:27px"></div>
<div class="rule h" style="left:295px;top:375px;width:245px"></div>
<div class="rule v" style="left:538px;top:350px;height:27px"></div>
<div class="rule h" style="left:538px;top:350px;width:184px"></div>
<div class="rule v" style="left:720px;top:350px;height:27px"></div>
<div class="rule h" style="left:720px;top:375px;width:204px"></div>
<div class="rule v" style="left:922px;top:350px;height:27px"></div>
<div class="rule h" style="left:922px;top:350px;width:196px"></div>

<div class="label" style="left:90px;top:333px"><div class="title">Picture Of Harvested Tendon</div><div class="desc">Decellularization,<br>lyophilization, and milling</div></div>
<div class="label" style="left:298px;top:358px"><div class="title">A Picture Of Milled Tendon Powder</div><div class="desc">Digestion with pepsin before<br>establishing physiologic pH and salinity</div></div>
<div class="label" style="left:543px;top:333px"><div class="title">A Picture Of Gel</div><div class="desc">Lyophilization of aliquots</div></div>
<div class="label" style="left:731px;top:358px"><div class="title">A picture of freeze-dried gel</div><div class="desc">Reconstitution with DI water</div></div>
<div class="label" style="left:926px;top:333px"><div class="title">A picture of reconstituted gel</div></div>
</body>
</html>
```